Seafood company needs a label design

Our brand name is Coral Tide Fisheries. We need a label design for a new product line of 200g trays of sardine fillets. The label/sleeve is going to wrap around the black tray. We are a family owned and operated business in Esperance, Western Australia. We would like simple appealing designs that catch the eye of the consumer.

Target Market(s)

seafood consumers in supermarkets

Colors

Designer to choose colors to be used in the design.

Requirements
Must have
• The front of the label must include
• •Coral Tide Fisheries
• •since 1997
• •Sustainably wild caught from the pristine southern ocean Esperance Western Australia
Nice to have
• Deep/Rich colours, and black, maybe Drawn picture of sardine/sardines or an anchor fast anchor.
Should not have
• cartoon images, not too cluttered

```html
<!DOCTYPE html>
<html lang="en">
<head>
<meta charset="utf-8">
<title>Coral Tide Fisheries – Tray Sleeve</title>
<link rel="stylesheet" href="https://fonts.googleapis.com/css2?family=Oswald:wght@400;600&display=swap">
<style>
  :root {
    --canvas-bg: #e9e9ea;
    --label-black: #050505;
    --label-glow: #2a2a2a;
    --band-teal: rgba(108, 184, 166, 0.95);
    --fish-teal-top: rgba(26, 165, 147, 0.55);
    --fish-teal-mid: rgba(20, 120, 108, 0.45);
    --deep-navy: #163a5e;
    --mustard: #d8b21c;
    --tag-green: #0f7e6a;
    --soft-grey: #d8d8d8;
  }
  * { margin: 0; padding: 0; box-sizing: border-box; }
  html, body {
    width: 1200px; height: 900px; overflow: hidden;
    background: var(--canvas-bg);
  }
  .sleeve {
    position: absolute;
    left: 383px; top: 108px;
    width: 435px; height: 685px;
    background: radial-gradient(ellipse 60% 45% at 55% 60%, var(--label-glow) 0%, var(--label-black) 75%);
    box-shadow: 0 8px 24px rgba(0,0,0,0.25);
    overflow: hidden;
  }
  .sardine-art {
    position: absolute;
    left: 2px; top: 70px;
    width: 136px; height: 560px;
    border-radius: 60px 60px 20px 20px;
    background: linear-gradient(180deg, var(--fish-teal-top) 0%, var(--fish-teal-mid) 60%, var(--fish-teal-top) 100%);
  }
  .brand-name {
    position: absolute;
    left: 150px; top: 178px;
    width: 285px;
    text-align: center;
    font-family: "Oswald", sans-serif;
    font-weight: 600;
    font-size: 48px; line-height: 1.1;
    letter-spacing: 1px;
    color: var(--mustard);
  }
  .since {
    position: absolute;
    left: 150px; top: 300px;
    width: 285px;
    text-align: center;
    font-family: "Oswald", sans-serif;
    font-weight: 400;
    font-size: 15px; line-height: 24px;
    letter-spacing: 5px;
    color: var(--soft-grey);
  }
  .origin-band {
    position: absolute;
    left: 100px; top: 456px;
    width: 335px; height: 108px;
    background: var(--band-teal);
    padding-top: 22px;
    text-align: center;
    font-family: "Oswald", sans-serif;
    font-weight: 600;
    line-height: 1.12;
  }
  .origin-band .claim { font-size: 19px; color: var(--tag-green); letter-spacing: 0.6px; }
  .origin-band .source { font-size: 14.5px; color: var(--deep-navy); letter-spacing: 0.3px; }
  .origin-band .place { font-size: 17px; color: var(--tag-green); letter-spacing: 0.5px; }
  .origin-band .rule {
    position: absolute;
    left: 0; right: 0; top: 92px;
    height: 1px;
    background: var(--tag-green);
  }
</style>
</head>
<body>
  <div class="sleeve">
    <div class="sardine-art" role="img" aria-label="Engraved-style teal illustration of a single sardine, head up"></div>

    <div class="brand-name">CORAL TIDE<br>FISHERIES</div>
    <div class="since">SINCE 1997</div>

    <div class="origin-band">
      <div class="claim">SUSTAINABLY WILD CAUGHT</div>
      <div class="source">FROM THE PRISTINE SOUTHERN OCEAN</div>
      <div class="place">ESPERANCE WESTERN AUSTRALIA</div>
      <div class="rule"></div>
    </div>
  </div>
</body>
</html>
```